TRENDY & MODERN BUSINESS CARD DESIGN for Media Company *

I need a minimalistic - clean - modern and professional business card layout and design for MEDIA & PHOTOGRAPHY STUDIO.

We do NOT have a logo, and not really looking for one - but rather excellent typography and design. We would consider the 3 as a focal point.

We do personal and commercial photography.

Target Market(s)

Personal and commercial photography clientele

Contact Information for Business Card

ZUB size - from zub.com / size guidelines are enclosed in the brief

Font styles to use
Sans Serif

Colors
f78f20
eda3c7
cee9f5
0555a3
e667a6
fbf289

Requirements
Must have
• Clean lines - Modern layout
Nice to have
• All blue background as an option - use color palette in brief please.
Should not have
• Old fashion fonts and regular fonts.

```html
<!DOCTYPE html>
<html lang="en">
<head>
<meta charset="utf-8">
<title>Halvern Media – Business Card</title>
<link rel="stylesheet" href="https://fonts.googleapis.com/css2?family=Lato:wght@300;400;700&family=Montserrat:wght@300;600&display=swap">
<style>
  :root {
    --brand-blue: #1559a6;
    --brand-pink: #e667a6;
    --soft-pink: #eda3c7;
    --ink: #111111;
    --ink-soft: #2a2a2a;
    --paper: #ffffff;
  }
  * { margin: 0; padding: 0; box-sizing: border-box; }
  html, body {
    width: 1004px; height: 1200px; overflow: hidden;
    background: var(--paper);
  }
  .canvas {
    position: relative;
    width: 800px; height: 956px;
    transform: scale(1.255);
    transform-origin: 0 0;
    font-family: "Lato", sans-serif;
    color: var(--ink);
  }
  .shapes { position: absolute; inset: 0; }
  .abs { position: absolute; white-space: nowrap; line-height: 1; }

  /* front */
  .website { right: 134px; top: 57px; font-size: 19px; font-weight: 300; letter-spacing: .3px; }
  .website .accent { color: var(--brand-pink); }

  .wordmark {
    font-family: "Montserrat", sans-serif;
    font-weight: 600;
    font-size: 32px;
    letter-spacing: 2.5px;
  }
  .tagline { font-family: "Montserrat", sans-serif; font-weight: 300; font-size: 19px; letter-spacing: .2px; }

  .front-wordmark { left: 132px; top: 224px; color: var(--ink); }
  .front-tagline { left: 132px; top: 264px; color: var(--ink); }

  .cities { color: #fff; font-size: 20px; font-weight: 300; }
  .cities .dot { color: var(--brand-pink); font-size: 17px; margin-right: 4px; }
  .cities-row-1 { left: 150px; top: 396px; }
  .cities-row-2 { left: 222px; top: 424px; }
  .city { margin-right: 18px; }

  /* back */
  .name-bar { position: absolute; left: 57px; top: 545px; width: 4px; height: 56px; background: var(--brand-pink); }
  .person-name { left: 72px; top: 543px; font-size: 31px; }
  .person-name .first { font-weight: 700; }
  .person-name .last { font-weight: 300; }
  .person-role { left: 72px; top: 583px; font-size: 20px; font-weight: 300; color: var(--ink-soft); }

  .contact { left: 114px; font-size: 21px; font-weight: 400; }
  .contact-phone { top: 711px; }
  .contact-email { top: 768px; }
  .contact-address { top: 816px; line-height: 26px; white-space: normal; width: 280px; }

  .back-wordmark { left: 444px; top: 684px; color: #fff; font-size: 31px; letter-spacing: 2px; }
  .back-tagline { left: 444px; top: 726px; color: #fff; font-size: 17px; }
</style>
</head>
<body>
<div class="canvas">

  <svg class="shapes" viewBox="0 0 800 956" width="800" height="956" aria-hidden="true">
    <rect x="684" y="64" width="104" height="6" fill="var(--brand-pink)"/>
    <polygon points="10,400 62,400 78,427 10,427" fill="var(--brand-pink)"/>
    <polygon points="530,427 552,400 788,400 788,427" fill="var(--brand-pink)"/>
    <rect x="10" y="427" width="778" height="45" fill="var(--brand-blue)"/>
    <polygon points="92,427 128,388 480,388 516,427" fill="var(--brand-blue)"/>

    <polygon points="458,490 493,490 418,712 493,933 458,933 383,712" fill="var(--soft-pink)"/>
    <polygon points="493,490 788,490 788,933 493,933 418,712" fill="var(--brand-blue)"/>
    <polygon points="400,645 418,645 395,712 418,778 400,778 370,712" fill="var(--brand-pink)"/>

    <g fill="var(--brand-pink)">
      <path d="M70,713 q0,-6 6,-7 h14 q6,1 6,7 v3 h-5 v-3 h-16 v3 h-5 z"/>
      <rect x="72" y="717" width="22" height="13" rx="2"/>
    </g>
    <g fill="none" stroke="var(--brand-pink)" stroke-width="1.6">
      <circle cx="83" cy="780" r="12"/>
      <ellipse cx="83" cy="780" rx="5" ry="12"/>
      <line x1="71" y1="780" x2="95" y2="780"/>
      <path d="M73,773 h20 M73,787 h20"/>
    </g>
    <path d="M83,858 C76,848 72,842 72,836 a11,11 0 0 1 22,0 c0,6 -4,12 -11,22 z" fill="var(--brand-pink)"/>
    <circle cx="83" cy="836" r="4.5" fill="#fff"/>
  </svg>

  <!-- front -->
  <p class="abs website">www.<span class="accent">halvernmedia</span>.com</p>

  <h1 class="abs wordmark front-wordmark">HALVERN MEDIA</h1>
  <p class="abs tagline front-tagline">FRAMING MOMENTS &amp; MAKING ART</p>

  <p class="abs cities cities-row-1">
    <span class="city"><span class="dot">o</span>Tampa</span><span class="city"><span class="dot">o</span>Chicago</span><span class="city"><span class="dot">o</span>Reno</span>
  </p>
  <p class="abs cities cities-row-2">
    <span class="city"><span class="dot">o</span>Tulum</span><span class="city"><span class="dot">o</span>Milano</span>
  </p>

  <!-- back -->
  <span class="name-bar"></span>
  <h2 class="abs person-name"><span class="first">Marisol</span> <span class="last">Vega</span></h2>
  <p class="abs person-role">Founder &amp; Media Director</p>

  <p class="abs contact contact-phone">(305) 555-0142</p>
  <p class="abs contact contact-email">mv@halvernmedia.com</p>
  <p class="abs contact contact-address">2200 Harbor Avenue<br>9th Floor, Bayview, FL 30000</p>

  <p class="abs wordmark back-wordmark">HALVERN MEDIA</p>
  <p class="abs tagline back-tagline">FRAMING MOMENTS &amp; MAKING ART</p>

</div>
</body>
</html>
```